Book cover design for a collection of poetry - The Lanternfield

Book cover and back design need to be moody, nostalgic, reflective, ethereal. Melancholy and other worldly. Cover design should not be time specific to a period or place but if applicable should reflect British landscape. Book cover should be in tones of blue and must include the title and author (THE LANTERNFIELD BY DORIAN WELKBRIDGE). We love the idea of rain, and looking out of a window. See attached designs. A world you are observing but not in.

Industry/Entity Type

Book Publisher

Font styles to use
Serif
Script

Colors
3176b5
3377b5
85acd3
eaf1f7
0792cd
33a6d7
86cae7
ecf7fb
86cfc6

Requirements
Must have
• The colour blue in it, must be melancholy and reflective.
Nice to have
• Rain in the cover.
Should not have
• Any bright colours.

```html
<!DOCTYPE html>
<html lang="en">
<head>
<meta charset="UTF-8">
<title>The Lanternfield — Book Cover Spread</title>
<link rel="stylesheet" href="https://fonts.googleapis.com/css2?family=Cinzel:wght@400;600;700&display=swap">
<style>
  :root {
    --stage-grey: #aaaaaa;
    --ink-navy: #0a1830;
    --deep-blue: #14335e;
    --mid-blue: #3176b5;
    --mist-blue: #85acd3;
    --fog-white: #eaf1f7;
    --title-blue: #1d4878;
    --text-white: #f4f7fa;
  }
  * { margin: 0; padding: 0; box-sizing: border-box; }
  html, body {
    width: 1200px;
    height: 1200px;
    overflow: hidden;
    background: var(--stage-grey);
  }
  .spread {
    position: absolute;
    left: 74px;
    top: 196px;
    width: 1054px;
    height: 808px;
    overflow: hidden;
  }
  .spread__backdrop {
    position: absolute;
    inset: 0;
    background:
      radial-gradient(ellipse 300px 230px at 870px 250px, rgba(234,241,247,0.95), rgba(234,241,247,0) 100%),
      radial-gradient(ellipse 420px 380px at 840px 360px, rgba(133,172,211,0.75), rgba(133,172,211,0) 100%),
      radial-gradient(ellipse 160px 260px at 780px 470px, rgba(20,51,94,0.55), rgba(20,51,94,0) 100%),
      linear-gradient(180deg, rgba(10,24,48,0) 55%, rgba(10,24,48,0.75) 100%),
      linear-gradient(90deg, var(--ink-navy) 0%, var(--deep-blue) 38%, #2c5a8c 62%, #4f7fae 100%);
  }
  .back-cover {
    position: absolute;
    left: 0;
    top: 0;
    width: 500px;
    height: 100%;
  }
  .back-cover__blurb {
    position: absolute;
    left: 30px;
    top: 163px;
    width: 455px;
    font-family: "Cinzel", serif;
    font-weight: 700;
    font-size: 12.5px;
    line-height: 20.6px;
    letter-spacing: 0.09em;
    color: var(--text-white);
    text-align: center;
    text-transform: uppercase;
  }
  .back-cover__blurb p + p { margin-top: 20.6px; }
  .back-cover__blurb em { font-style: italic; }
  .spine {
    position: absolute;
    left: 500px;
    top: 0;
    width: 50px;
    height: 100%;
  }
  .spine__text {
    position: absolute;
    left: 50%;
    top: 404px;
    transform: translate(-50%, -50%) rotate(90deg);
    white-space: nowrap;
    font-family: "Cinzel", serif;
    font-weight: 400;
    font-size: 25px;
    letter-spacing: 0.16em;
    color: var(--text-white);
  }
  .spine__gap { display: inline-block; width: 18px; }
  .front-cover {
    position: absolute;
    left: 550px;
    top: 0;
    width: 504px;
    height: 100%;
    text-align: center;
  }
  .front-cover__title {
    position: absolute;
    left: 0;
    right: 0;
    top: 118px;
    font-family: "Cinzel", serif;
    font-weight: 700;
    font-size: 44px;
    line-height: 70px;
    letter-spacing: 0.1em;
    color: var(--title-blue);
  }
  .front-cover__byline {
    position: absolute;
    left: 0;
    right: 0;
    top: 676px;
    font-family: "Cinzel", serif;
    font-weight: 400;
    font-size: 21px;
    line-height: 37px;
    letter-spacing: 0.1em;
    color: var(--text-white);
  }
</style>
</head>
<body>
  <main class="spread">
    <div class="spread__backdrop" role="img" aria-label="Rain-streaked window pane in deep blues, with a misty pale sky and a bare tree blurred behind the glass"></div>

    <section class="back-cover">
      <div class="back-cover__blurb">
        <p><em>The Lanternfield</em> is a collection of poetry.</p>
        <p>Told in two parts we first meet Charles<br>
        – aged, crippled and left alone in his<br>
        inherited marsh house – reflecting on<br>
        his life and his marriage to beautiful<br>
        Alice who we meet in part two.<br>
        Alice is suicidal, manically depressed and<br>
        struggling with life as a wife and<br>
        mother. She meets, harbors and falls in<br>
        love with a soldier during WWII and her<br>
        world is changed forever.</p>
        <p>Moving through the 20th century,<br>
        this life and the next, The Lanternfield<br>
        interweaves grief, loss, the after-life,<br>
        mental illness, and ultimately<br>
        the true nature of love.</p>
      </div>
    </section>

    <section class="spine">
      <div class="spine__text">THE LANTERNFIELD<span class="spine__gap"></span>DORIAN WELKBRIDGE</div>
    </section>

    <section class="front-cover">
      <h1 class="front-cover__title">THE<br>LANTERNFIELD</h1>
      <p class="front-cover__byline">BY<br>DORIAN WELKBRIDGE</p>
    </section>
  </main>
</body>
</html>
```